Letterhead for small civil engineer company

We need bold and modern design for company letterhead in MS word. It needs to have company logo and company info. Somewhere in the upper right part of document needs to be space for "recever" and the documents starts with, example, "SUBJECT: CIVIL ENGINEER LETTERHEAD".

in the bottom part of document needs to be signature and date.

Company info: Veltrana d.o.o., Lipovac 15, Lipovac (Općina Brdarić), OIB 47396028154, www.veltrana.hr, info@veltrana.hr

Email of document sender needs to be somewhere if document, exapmle xyz@veltrana.hr

Target Market(s)

Civil engineer company and projects

Industry/Entity Type

Civil engineer

Font styles to use
Serif

Colors
F0912C
F2A743
F7CA91
FBE8D2
FDF5EE

Requirements
Must have
• Company logo and company info
Nice to have
• Moder and clean design
Should not have
• Too much details

```html
<!DOCTYPE html>
<html lang="en">
<head>
<meta charset="utf-8">
<title>Veltrana d.o.o. – Stationery</title>
<link rel="stylesheet" href="https://fonts.googleapis.com/css2?family=Source+Sans+3:wght@400;600;700&display=swap">
<style>
  :root {
    --backdrop: #3a3a3c;
    --paper: #ffffff;
    --orange: #e88d35;
    --orange-text: #e98a2e;
    --grey-band: #666666;
    --grey-mark: #6f6f6f;
    --ink: #2d2d2d;
    --label: #f2f2f2;
    --signature-tone: #2b3a8f;
  }
  html, body {
    margin: 0;
    padding: 0;
    overflow: hidden;
    background: var(--backdrop);
  }
  .stationery-set {
    width: 1200px;
    height: 778px;
    display: block;
    font-family: "Source Sans 3", sans-serif;
  }
  .paper { fill: var(--paper); filter: drop-shadow(1px 2px 2px rgba(0,0,0,.45)); }
  .band-orange { fill: var(--orange); }
  .band-grey { fill: var(--grey-band); }
  .rule { stroke: var(--orange); stroke-width: 0.8; }
  .mark-square { fill: none; stroke: var(--grey-mark); stroke-width: 1.4; }
  .mark-square.on-orange { stroke: var(--grey-band); }
  .wordmark { fill: var(--orange-text); font-weight: 600; letter-spacing: .06em; }
  .wordmark.on-orange { fill: var(--paper); }
  .subject-label { fill: var(--orange-text); font-weight: 700; font-size: 9.5px; }
  .subject-text { fill: var(--ink); font-weight: 600; font-size: 12px; }
  .date-label { fill: var(--orange-text); font-weight: 700; font-size: 8px; }
  .company-name { fill: var(--paper); font-weight: 700; letter-spacing: .03em; }
  .footer-text { fill: var(--paper); font-size: 7px; }
  .footer-link { fill: var(--paper); font-size: 7px; font-weight: 700; letter-spacing: .04em; }
  .icon { fill: var(--orange); }
  .view-label { fill: var(--label); font-size: 12px; letter-spacing: .04em; }
  .pill { fill: none; stroke: var(--grey-mark); stroke-width: .7; }
  .pill-solid { fill: var(--grey-band); }
  .pill-text { fill: var(--grey-mark); font-size: 5.5px; letter-spacing: .14em; }
  .pill-text.light { fill: var(--paper); font-weight: 700; }
  .card-small { fill: var(--paper); font-size: 5px; }
  .signature-area { fill: var(--signature-tone); opacity: .18; }
</style>
</head>
<body>
<svg class="stationery-set" viewBox="0 0 1200 778" xmlns="http://www.w3.org/2000/svg">
  <defs>
    <linearGradient id="card-texture" x1="0" y1="0" x2="1" y2="1">
      <stop offset="0" stop-color="#e6e4df"/>
      <stop offset=".55" stop-color="#f7f6f3"/>
      <stop offset="1" stop-color="#ffffff"/>
    </linearGradient>
  </defs>

  <!-- Letterhead -->
  <g class="letterhead">
    <rect class="paper" x="102" y="94" width="454" height="589"/>
    <rect class="mark-square" x="169" y="129" width="39" height="39"/>
    <text class="wordmark" x="134" y="186" font-size="16">VELTRANA</text>
    <line class="rule" x1="134" y1="196" x2="518" y2="196"/>
    <text x="134" y="257"><tspan class="subject-label">SUBJECT: </tspan><tspan class="subject-text">Civil Engineer  Letterhead</tspan></text>
    <rect class="signature-area" x="387" y="571" width="82" height="27" rx="3" role="img" aria-label="Handwritten signature"/>
    <text class="date-label" x="392" y="612">Date:</text>
    <polygon class="band-grey" points="264,641 556,641 556,668 254,668"/>
    <polygon class="band-orange" points="102,633 288,633 270,659 102,659"/>
    <text class="company-name" x="133" y="652" font-size="15.5">Veltrana d.o.o.</text>
    <text class="footer-text" x="308" y="653">Lipovac 15, Lipovac (Općina Brdarić), OIB 47396028154,</text>
    <circle class="icon" cx="302" cy="661" r="3"/>
    <text class="footer-link" x="308" y="663.5">www.veltrana.hr</text>
    <rect class="icon" x="379" y="658" width="6" height="5" rx="1"/>
    <text class="footer-link" x="389" y="663.5">info@veltrana.hr</text>
  </g>

  <!-- Business card front -->
  <g class="card-front">
    <text class="view-label" x="842" y="88" text-anchor="middle">Front</text>
    <rect class="paper" x="756" y="97" width="187" height="107" fill="url(#card-texture)" style="fill:url(#card-texture)"/>
    <rect class="mark-square" x="834" y="109" width="25" height="25"/>
    <text class="wordmark" x="847" y="147" font-size="10" text-anchor="middle">VELTRANA</text>
    <rect class="pill" x="810" y="158" width="74" height="10" rx="5"/>
    <text class="pill-text" x="847" y="165" text-anchor="middle">info@veltrana.hr</text>
    <polygon class="band-grey" points="866,187 943,187 943,198 857,198"/>
    <polygon class="band-orange" points="756,181 880,181 869,193 756,193"/>
    <text class="card-small" x="764" y="189.5">Lipovac 15, Lipovac (Općina Brdarić)</text>
    <text class="card-small" x="881" y="195">OIB 47396028154</text>
  </g>

  <!-- Business card back -->
  <g class="card-back">
    <rect class="band-orange" x="754" y="218" width="187" height="107"/>
    <rect class="mark-square on-orange" x="834" y="241" width="25" height="25"/>
    <text class="wordmark on-orange" x="847" y="279" font-size="10" text-anchor="middle">VELTRANA</text>
    <rect class="pill-solid" x="805" y="303" width="85" height="11" rx="5.5"/>
    <text class="pill-text light" x="847.5" y="310.5" text-anchor="middle">www.veltrana.hr</text>
    <text class="view-label" x="843" y="346" text-anchor="middle">Back</text>
  </g>

  <!-- Envelope -->
  <g class="envelope">
    <path class="band-orange" d="M589 374 H1107 L1078 414 Q1064 434 1040 434 H640 Q615 434 604 414 Z"/>
    <text class="wordmark on-orange" x="848" y="395" font-size="8" text-anchor="middle">VELTRANA</text>
    <rect class="mark-square on-orange" x="838" y="399" width="20" height="20"/>

    <rect class="paper" x="584" y="448" width="520" height="233"/>
    <rect class="mark-square" x="634" y="467" width="36" height="36"/>
    <text class="wordmark" x="600" y="520" font-size="15">VELTRANA</text>
    <polygon class="band-grey" points="714,646 1104,646 1104,671 704,671"/>
    <polygon class="band-orange" points="584,638 745,638 727,663 584,663"/>
    <text class="company-name" x="606" y="655" font-size="11.5">Veltrana d.o.o.</text>
    <text class="footer-text" x="747" y="661">Lipovac 15, Lipovac (Općina Brdarić), OIB 47396028154</text>
    <circle class="icon" cx="923" cy="657.5" r="3.5"/>
    <text class="footer-link" x="930" y="661">www.veltrana.hr</text>
    <rect class="icon" x="1006" y="654" width="7" height="6" rx="1"/>
    <text class="footer-link" x="1017" y="661">info@veltrana.hr</text>
  </g>
</svg>
</body>
</html>
```